Wanderlark Gin - Bottle Label for a craft Gin about to be launched on the world from New Zealand

We are a start up craft distillery in New Zealand. We have developed a wonderful Gin using our own grain spirit and both traditional and New Zealand native botanicals (Manuka to be specific), chosen our bottle and the name "Wanderlark" and done a bit of amateur label design and now we are looking for someone to make it great.

Feel free to change up our amateur concept but give us something that will pop from the back bar and scream authenticity, craft and individuality.

The attached files give you the specifications of the bottle, our current concept for a Wanderlark label and an earlier concept drawing that gives an idea of where we are thinking the two labels should go on the front of the bottle.

Thanks, we look forward to your ideas!!

Target Market(s)

High end and craft Gin drinkers. Hipsters and cocktail barflys and their bar tenders and bar owners

Font styles to use
Serif
Sans Serif
Decorative
Script

Requirements
Must have
• Attractive individuality
Nice to have
• Coolness
Should not have
• Uncoolness

```html
<!DOCTYPE html>
<html lang="en">
<head>
<meta charset="utf-8">
<title>Wanderlark Gin – Label Concept</title>
<link rel="stylesheet" href="https://fonts.googleapis.com/css2?family=Anton&family=Oswald:wght@400;500&display=swap">
<style>
  :root {
    --paper: #ffffff;
    --grid: #e6e6e6;
    --ink: #000000;
    --white: #ffffff;
    --lemon: #f5ec1c;
    --berry: #ee2027;
    --aqua: #2ee6ee;
    --orchid: #d9368f;
    --leaf: #46a81b;
    --display: "Anton", "Oswald", sans-serif;
    --body: "Oswald", "Arial Narrow", sans-serif;
  }
  html, body {
    margin: 0;
    padding: 0;
    width: 1155px;
    height: 1200px;
    overflow: hidden;
    background: var(--paper);
  }
  .board {
    position: relative;
    width: 1155px;
    height: 1200px;
    background-color: var(--paper);
    background-image:
      linear-gradient(var(--grid) 1px, transparent 1px),
      linear-gradient(90deg, var(--grid) 1px, transparent 1px);
    background-size: 30.4px 30.4px;
  }
  .artwork {
    position: absolute;
    left: 0;
    top: 0;
  }
  .note { font-family: var(--display); font-size: 30px; fill: var(--ink); }
  .label-title { font-family: var(--display); font-size: 100px; fill: var(--ink); }
  .label-tagline { font-family: var(--body); font-size: 22px; fill: var(--white); }
  .label-volume { font-family: var(--body); font-size: 28px; fill: var(--lemon); }
  .badge-figure { font-family: var(--display); font-size: 26px; fill: var(--white); }
  .badge-unit { font-family: var(--body); font-weight: 500; font-size: 14px; fill: var(--white); }
  .recipe-word { font-family: var(--display); font-size: 22px; fill: var(--white); }
  .recipe-number { font-family: var(--display); font-size: 60px; fill: var(--white); }
  .back-copy { font-family: var(--body); font-size: 18px; fill: var(--white); }
</style>
</head>
<body>
<main class="board">
  <svg class="artwork" width="1155" height="1200" viewBox="0 0 1155 1200" xmlns="http://www.w3.org/2000/svg">
    <defs>
      <linearGradient id="infusion" x1="0" y1="0" x2="1" y2="0.4">
        <stop offset="0" stop-color="var(--berry)"/>
        <stop offset="0.35" stop-color="var(--lemon)"/>
        <stop offset="0.55" stop-color="var(--orchid)"/>
        <stop offset="0.75" stop-color="var(--aqua)"/>
        <stop offset="1" stop-color="var(--lemon)"/>
      </linearGradient>
    </defs>

    <text class="note note--front" x="80" y="124" textLength="760" lengthAdjust="spacingAndGlyphs">color scheme reminiscent of flavor infusions + a cool dead cat</text>
    <text class="note note--back" x="730" y="774" textLength="290" lengthAdjust="spacingAndGlyphs">color and number coded</text>

    <g class="front-label">
      <polygon class="front-label__shape" points="392,198 790,228 866,438 812,640 378,590 282,418" fill="var(--ink)"/>
      <rect class="front-label__art" role="img" aria-label="Cat silhouette filled with colourful botanical flower pattern"
            x="306" y="232" width="506" height="280" rx="60" fill="url(#infusion)"/>
      <text class="label-title" x="414" y="404" textLength="376" lengthAdjust="spacingAndGlyphs">WANDERLARK</text>
      <text class="label-tagline" x="597" y="557" text-anchor="middle" textLength="406" lengthAdjust="spacingAndGlyphs">A classically inspired Gin with a New Zealand twist</text>
      <text class="label-volume" x="604" y="596" text-anchor="middle">500ml</text>
    </g>

    <g class="back-label">
      <polygon class="back-label__shape" points="398,862 758,862 736,1080 418,1080" fill="var(--ink)"/>

      <g class="badge badge--proof">
        <circle cx="486" cy="856" r="41" fill="var(--ink)"/>
        <circle cx="486" cy="856" r="35" fill="none" stroke="var(--white)" stroke-width="2.5"/>
        <text class="badge-figure" x="486" y="864" text-anchor="middle">84</text>
        <text class="badge-unit" x="486" y="881" text-anchor="middle">proof</text>
      </g>

      <g class="badge badge--abv">
        <circle cx="669" cy="858" r="41" fill="var(--ink)"/>
        <circle cx="669" cy="858" r="35" fill="none" stroke="var(--white)" stroke-width="2.5"/>
        <text class="badge-figure" x="669" y="864" text-anchor="middle" textLength="50" lengthAdjust="spacingAndGlyphs">42%</text>
        <text class="badge-unit" x="669" y="882" text-anchor="middle">vol</text>
      </g>

      <g class="badge badge--recipe">
        <circle cx="578" cy="854" r="66" fill="var(--ink)"/>
        <circle cx="578" cy="854" r="61" fill="var(--white)"/>
        <circle cx="578" cy="854" r="57" fill="var(--leaf)"/>
        <text class="recipe-word" x="578" y="832" text-anchor="middle">recipe</text>
        <text class="recipe-number" x="578" y="893" text-anchor="middle">#3</text>
      </g>

      <g class="back-copy-block">
        <text class="back-copy" x="577" y="948" text-anchor="middle">Distilled in-house starting with local grain and</text>
        <text class="back-copy" x="577" y="972" text-anchor="middle">finished with 11 botanicals including a</text>
        <text class="back-copy" x="577" y="997" text-anchor="middle">generous helping of East Coast Manuka cones,</text>
        <text class="back-copy" x="567" y="1021" text-anchor="middle">Gisborne Citrus and Otago Lavender</text>
      </g>

      <rect class="back-label__band" x="424" y="1054" width="308" height="12" fill="var(--leaf)"/>
    </g>
  </svg>
</main>
</body>
</html>
```